6 page business brochure/report design

Hi Everyone,

I need someone to take my word document and make a corporate business brochure/report with a title page and 4 pages of content and then the back page. (6 pages in total). I will be providing the text, logo and web link to the website ([login to view URL]).

I have also mocked up a title page for the type of corporate style I am looking for.

The final product should feel professionally constructed, be of a corporate style and match a similar style of our website

The final file to be delivered in Indesign or similar and any images used should be free stock photography. Red text on the word document is for guidance and should not be included.

```html
<!DOCTYPE html>
<html lang="en">
<head>
<meta charset="utf-8">
<title>Veridra Business Plan 2019 – Brochure Spreads</title>
<link rel="stylesheet" href="https://fonts.googleapis.com/css2?family=Montserrat:wght@300;400;600;700;800&family=Open+Sans:wght@400;600&display=swap">
<style>
  :root {
    --bg: #e6e6e6;
    --navy: #1c3350;
    --navy-deep: #15283f;
    --teal: #1f6a87;
    --teal-light: #2c88a6;
    --sheet: #f1f4f7;
    --sheet-edge: #dfe6ec;
    --heading: #1f78c1;
    --text: #3a4450;
    --table-dark: #5d6066;
    --table-row: #6c7076;
    --arrow: #565656;
    --white: #ffffff;
  }
  * { box-sizing: border-box; margin: 0; padding: 0; }
  html, body { width: 1200px; height: 2236px; overflow: hidden; }
  body {
    position: relative;
    background: var(--bg);
    font-family: "Open Sans", Arial, sans-serif;
    color: var(--text);
  }

  .spread {
    position: absolute;
    left: 60px;
    width: 960px;
    height: 679px;
    display: flex;
    box-shadow: 0 14px 30px rgba(0,0,0,.18);
  }
  .spread--first  { top: 20px; }
  .spread--cover  { top: 759px; }
  .spread--third  { top: 1498px; }

  .page {
    position: relative;
    width: 480px;
    height: 679px;
    background: var(--navy);
    overflow: hidden;
  }
  .page + .page { border-left: 1px solid rgba(0,0,0,.25); }
  .page__decor { position: absolute; inset: 0; width: 100%; height: 100%; }

  .sheet {
    position: absolute;
    top: 30px; bottom: 44px;
    background: linear-gradient(160deg, var(--white), var(--sheet) 60%, var(--sheet-edge));
    border-radius: 3px;
    padding: 26px 26px 20px;
  }
  .page--left .sheet  { left: 30px; right: 14px; }
  .page--right .sheet { left: 14px; right: 30px; }

  .section-title {
    font-family: "Montserrat", Arial, sans-serif;
    font-weight: 800;
    color: var(--heading);
    font-size: 15px;
    margin-bottom: 6px;
  }
  .section-title--sub { font-size: 13px; font-weight: 700; margin-top: 10px; }
  .page-title {
    font-family: "Montserrat", Arial, sans-serif;
    font-weight: 800;
    font-size: 30px;
    color: var(--heading);
    text-align: center;
    margin-bottom: 14px;
  }
  .body-text { font-size: 9px; line-height: 1.5; margin-bottom: 8px; }
  .body-text--note { font-size: 8px; font-weight: 600; color: var(--navy); }

  /* Glance page */
  .glance { display: flex; gap: 16px; }
  .glance__intro { flex: 1; }
  .glance__key { width: 168px; }
  .key-data { width: 100%; border-collapse: collapse; font-size: 8px; color: var(--white); }
  .key-data td { padding: 5px 5px; border-bottom: 1px solid rgba(255,255,255,.35); background: var(--table-row); }
  .key-data td:first-child { background: var(--table-dark); font-weight: 600; width: 44%; }

  .fin-caption { font-family: "Montserrat", Arial, sans-serif; font-weight: 700; font-size: 9px; color: var(--navy); margin: 16px 0 5px; }
  .fin-table { width: 100%; border-collapse: collapse; font-size: 8px; }
  .fin-table th { background: var(--table-dark); color: var(--white); font-weight: 600; padding: 5px 4px; text-align: right; }
  .fin-table th:first-child, .fin-table td:first-child { text-align: left; }
  .fin-table td { padding: 4px; text-align: right; border-bottom: 1px solid #cfd6dd; }
  .fin-table tr:nth-child(even) td { background: #e3e8ed; }
  .fin-table .total td { font-weight: 700; color: var(--navy); }

  /* Cover spread */
  .page--back { background: var(--navy); }
  .back__content { position: absolute; top: 52px; left: 40px; right: 44px; color: var(--white); }
  .back__title { font-family: "Montserrat", Arial, sans-serif; font-weight: 800; font-size: 30px; margin-bottom: 18px; }
  .back__content .body-text { font-size: 9.5px; line-height: 1.6; margin-bottom: 12px; color: #dce6ef; }

  .page--cover { background: var(--navy-deep); }
  .cover__titles { position: absolute; top: 54px; left: 56px; right: 30px; }
  .cover__brand { font-family: "Montserrat", Arial, sans-serif; font-weight: 300; font-size: 54px; color: #4aa3d6; letter-spacing: 2px; line-height: 1; }
  .cover__plan { font-family: "Montserrat", Arial, sans-serif; font-weight: 800; font-size: 26px; color: var(--white); margin-top: 12px; line-height: 1.15; }

  /* Third spread */
  .challenge { display: flex; gap: 12px; margin: 6px 0 10px; }
  .challenge__photo { width: 150px; height: 104px; background: linear-gradient(135deg, #2d3d52, #6b7788 50%, #3c4a5e); }
  .callout {
    flex: 1; border: 1.5px solid var(--teal-light); padding: 10px 12px;
    font-family: "Montserrat", Arial, sans-serif; color: var(--teal);
  }
  .callout__figure { font-size: 14px; font-weight: 700; line-height: 1.2; }
  .callout__source { font-size: 7px; color: var(--text); margin-top: 6px; font-family: "Open Sans", Arial, sans-serif; }
  .callout__plus { font-size: 18px; font-weight: 700; line-height: 1; float: right; }

  .split { display: flex; gap: 18px; }
  .split > div { flex: 1; }

  .flow-arrow { position: absolute; left: 1085px; width: 70px; height: 110px; }
</style>
</head>
<body>

<!-- Flow arrows -->
<svg class="flow-arrow" style="top:40px" viewBox="0 0 70 110" aria-hidden="true">
  <rect x="31" y="0" width="8" height="74" fill="var(--arrow)"/>
  <polygon points="0,70 70,70 35,110" fill="var(--arrow)"/>
</svg>
<svg class="flow-arrow" style="top:628px" viewBox="0 0 70 110" aria-hidden="true">
  <rect x="31" y="36" width="8" height="74" fill="var(--arrow)"/>
  <polygon points="0,40 70,40 35,0" fill="var(--arrow)"/>
</svg>
<svg class="flow-arrow" style="top:1360px" viewBox="0 0 70 110" aria-hidden="true">
  <rect x="31" y="0" width="8" height="74" fill="var(--arrow)"/>
  <polygon points="0,70 70,70 35,110" fill="var(--arrow)"/>
</svg>

<!-- Spread 1: At a glance / Operations -->
<section class="spread spread--first">
  <article class="page page--left">
    <svg class="page__decor" viewBox="0 0 480 679" preserveAspectRatio="none" aria-hidden="true">
      <polygon points="0,520 0,679 300,679" fill="var(--teal)"/>
      <polygon points="0,0 160,0 0,140" fill="var(--teal)" opacity=".6"/>
    </svg>
    <div class="sheet">
      <div class="glance">
        <div class="glance__intro">
          <h2 class="section-title">Veridra at a glance</h2>
          <p class="body-text">Veridra is a digital insurance claims handling platform that connects motorists, insurers and repairers in one place, reducing the time and cost of settling every vehicle claim.</p>
          <p class="body-text">Veridra is seeking to raise £450,000 in return for equity. Funds will support platform growth, new partner onboarding and the launch of our marketplace across the UK during the coming year.</p>
        </div>
        <div class="glance__key">
          <h2 class="section-title">Key Data</h2>
          <table class="key-data">
            <tr><td>Company name</td><td>Veridra Ltd</td></tr>
            <tr><td>Sector</td><td>Insurance technology</td></tr>
            <tr><td>Founded</td><td>2017</td></tr>
            <tr><td>Raise</td><td>£450,000</td></tr>
            <tr><td>Equity offered</td><td>15%</td></tr>
            <tr><td>Pre-money</td><td>£2,550,000</td></tr>
            <tr><td>Tax relief</td><td>EIS eligible</td></tr>
          </table>
        </div>
      </div>
      <h3 class="fin-caption">Financial Overview</h3>
      <table class="fin-table">
        <tr><th>Year</th><th>2019</th><th>2020</th><th>2021</th><th>2022</th></tr>
        <tr><td>Sales</td><td>0</td><td>214,000</td><td>1,101,000</td><td>2,870,000</td></tr>
        <tr><td>Cost of Sales</td><td>0</td><td>38,000</td><td>182,000</td><td>460,000</td></tr>
        <tr><td>Gross profit</td><td>0</td><td>176,000</td><td>919,000</td><td>2,410,000</td></tr>
        <tr><td>Overheads</td><td>417,000</td><td>540,000</td><td>690,000</td><td>905,000</td></tr>
        <tr class="total"><td>Pre-tax profit</td><td>-417,000</td><td>-364,000</td><td>229,000</td><td>1,505,000</td></tr>
      </table>
      <p class="body-text body-text--note" style="margin-top:10px">Please note a £17,500 loan has been repaid from capital raised in 2018, and the platform was valued at £2.55m in December 2018.</p>
    </div>
  </article>

  <article class="page page--right">
    <svg class="page__decor" viewBox="0 0 480 679" preserveAspectRatio="none" aria-hidden="true">
      <polygon points="480,0 300,0 480,170" fill="var(--teal)" opacity=".6"/>
      <polygon points="200,679 480,520 480,679" fill="var(--teal)"/>
    </svg>
    <div class="sheet">
      <h1 class="page-title">Operations</h1>
      <h2 class="section-title section-title--sub">How It Works</h2>
      <p class="body-text">Veridra is a modular claims platform that allows insurers to streamline and simplify their processes. Customers report incidents through a guided mobile journey and every party follows the claim in real time.</p>
      <h2 class="section-title section-title--sub">Claims handling algorithm</h2>
      <p class="body-text">Our proprietary algorithm handles claims based on the content of each incident report. Photos, location data and vehicle details are checked automatically, so simple claims are approved in minutes while complex cases go straight to a specialist handler.</p>
      <h2 class="section-title section-title--sub">Partner Ecosystem / Marketplace</h2>
      <p class="body-text">Once a claim is approved, the platform matches the vehicle to the closest approved repairer. Garages, recovery firms and parts suppliers bid for work in the marketplace, giving insurers better prices and motorists faster repairs.</p>
    </div>
  </article>
</section>

<!-- Spread 2: Back cover / Front cover -->
<section class="spread spread--cover">
  <article class="page page--left page--back">
    <svg class="page__decor" viewBox="0 0 480 679" preserveAspectRatio="none" aria-hidden="true">
      <polygon points="0,420 480,330 480,679 0,679" fill="var(--teal)"/>
      <polygon points="0,560 480,470 480,679 0,679" fill="var(--teal-light)" opacity=".55"/>
      <polygon points="300,679 480,500 480,679" fill="var(--navy)" opacity=".5"/>
    </svg>
    <div class="back__content">
      <h2 class="back__title">Risk Warning</h2>
      <p class="body-text">Investing in small private companies involves risks, including illiquidity, lack of dividends, loss of investment and dilution, and it should be done only as part of a diversified portfolio.</p>
      <p class="body-text">This document has been approved as a financial promotion by Seedline Partners Ltd, which is authorised and regulated by the Financial Conduct Authority. Seedline Partners has not verified all information provided by the company.</p>
      <p class="body-text">The availability of any tax relief, including EIS and SEIS, depends on the individual circumstances of each investor and of the company concerned, and may be subject to change in the future.</p>
    </div>
  </article>

  <article class="page page--right page--cover">
    <svg class="page__decor" viewBox="0 0 480 679" preserveAspectRatio="none">
      <defs>
        <linearGradient id="tower" x1="0" y1="0" x2="1" y2="1">
          <stop offset="0" stop-color="#8d99a6"/>
          <stop offset=".5" stop-color="#4b5868"/>
          <stop offset="1" stop-color="#2a3646"/>
        </linearGradient>
      </defs>
      <polygon points="40,330 480,250 480,679 130,679" fill="url(#tower)" role="img" aria-label="Photograph of glass office towers seen from below"/>
      <polygon points="0,400 110,470 150,679 0,679" fill="var(--teal)"/>
      <polygon points="0,540 150,679 0,679" fill="var(--teal-light)" opacity=".7"/>
    </svg>
    <div class="cover__titles">
      <div class="cover__brand">Veridra</div>
      <div class="cover__plan">BUSINESS PLAN<br>2019</div>
    </div>
  </article>
</section>

<!-- Spread 3: Market / Revenue -->
<section class="spread spread--third">
  <article class="page page--left">
    <svg class="page__decor" viewBox="0 0 480 679" preserveAspectRatio="none" aria-hidden="true">
      <polygon points="0,520 0,679 300,679" fill="var(--teal)"/>
      <polygon points="0,0 160,0 0,140" fill="var(--teal)" opacity=".6"/>
    </svg>
    <div class="sheet">
      <h2 class="section-title">Market Overview</h2>
      <p class="body-text">According to industry research, the UK motor claims market is worth over £10bn each year. More than two million vehicle claims are filed annually, and most are still handled by phone, paper forms and email.</p>
      <p class="body-text">Veridra is positioned at the intersection of insurance and repair, offering one digital workflow for every party involved in a claim.</p>
      <h2 class="section-title">The Challenge &amp; Need</h2>
      <p class="body-text">Insurers face rising costs and slow settlement times. It takes an average of 30 days to handle a straightforward claim, and customers frequently cite poor communication as the main reason for switching provider at renewal.</p>
      <div class="challenge">
        <div class="challenge__photo" role="img" aria-label="Photograph of congested city traffic"></div>
        <div class="callout">
          <span class="callout__plus">+</span>
          <div class="callout__figure">It takes on average 30 days to handle a claim</div>
          <div class="callout__source">Source: industry claims survey 2018</div>
        </div>
      </div>
      <p class="body-text">Based on our discussions with claims handlers and insurance executives, we expect to reduce handling time by up to 70% and lower the cost of each claim for insurers, repairers and drivers alike.</p>
    </div>
  </article>

  <article class="page page--right">
    <svg class="page__decor" viewBox="0 0 480 679" preserveAspectRatio="none" aria-hidden="true">
      <polygon points="480,0 300,0 480,170" fill="var(--teal)" opacity=".6"/>
      <polygon points="200,679 480,520 480,679" fill="var(--teal)"/>
    </svg>
    <div class="sheet">
      <h2 class="section-title">Revenue</h2>
      <p class="body-text">Veridra is a B2B business serving insurers and repair networks. Revenue is generated via a subscription fee per user and a transaction fee on every claim processed through the marketplace.</p>
      <h2 class="section-title">Competitors</h2>
      <p class="body-text">We believe there are three types of competing solution: legacy claims software, in-house insurer tools and small repair marketplaces. None of them connects every party in one place or uses automated claim assessment.</p>
      <p class="body-text">Our platform is modular, so insurers can adopt a single feature first and add more later. This lowers switching costs and shortens the sales cycle compared with large software suites.</p>
      <h2 class="section-title">Fund Raise</h2>
      <h3 class="section-title section-title--sub" style="margin-top:0;font-size:10px;color:var(--navy)">Use of Funds</h3>
      <p class="body-text">We are looking to raise £450,000. Funds will be used for product development, sales and marketing, and working capital over the next eighteen months.</p>
      <div class="split">
        <div>
          <h2 class="section-title">Outstanding Debt</h2>
          <p class="body-text">The company has a £17,500 director loan that will be repaid from future revenue, not from this raise.</p>
        </div>
        <div>
          <h2 class="section-title">Exit Strategy</h2>
          <p class="body-text">Our target exit is a trade sale to an insurer or software group within five years.</p>
        </div>
      </div>
    </div>
  </article>
</section>

</body>
</html>
```